Super urgent - business card design

I need to design a business card
on the front side the words "VORIAN PARTNERS" with the top half surrounded by a stylised cloud. Minimalist, navy blue font on white background, with the Vorian partners in embossing.

On the back contact details (avoid centered). I would rather have the details taking the 2/3rd on the right and having the logo on the left, but anyway not plain centered

Marcello Tavoletti
CEO e Fondatore

m.tavoletti@vorian-partners.example
+39.331.584.2064

Piazza Lunetti 7
20145 Milano

```html
<!DOCTYPE html>
<html lang="it">
<head>
<meta charset="utf-8">
<title>Vorian Partners — Business Card</title>
<link href="https://fonts.googleapis.com/css2?family=Playfair+Display:wght@700&family=Montserrat:wght@400&display=swap" rel="stylesheet">
<style>
  :root {
    --backdrop: #d1d6d6;
    --paper: #efefed;
    --navy: #142a4c;
    --ink-soft: #2a3a55;
    --edge: #142a4c;
  }
  * { box-sizing: border-box; margin: 0; padding: 0; }
  html, body {
    width: 1200px; height: 881px; overflow: hidden;
    background: var(--backdrop);
  }
  .stage { position: relative; width: 1200px; height: 881px; }

  .card {
    position: absolute;
    width: 500px; height: 286px;
    background: var(--paper);
    border-radius: 2px;
    box-shadow: 0 18px 30px rgba(40, 50, 60, 0.18), 0 2px 4px rgba(40, 50, 60, 0.12);
    color: var(--navy);
  }
  .card--front { left: 630px; top: 250px; border-bottom: 5px solid var(--edge); }
  .card--back  { left: 80px;  top: 350px; }

  .wordmark {
    font-family: "Playfair Display", Georgia, serif;
    font-weight: 700;
    color: var(--navy);
    text-transform: uppercase;
    line-height: 1.05;
  }
  .wordmark span { display: block; }
  .wordmark .line-one { letter-spacing: 0.16em; }
  .wordmark .line-two { letter-spacing: 0.04em; }

  .card--front .wordmark {
    position: absolute; left: 0; right: 0; top: 72px;
    text-align: center; font-size: 58px;
  }

  .card--back .wordmark {
    position: absolute; right: 34px; top: 40px;
    font-size: 38px; text-align: left;
  }

  .contact {
    position: absolute; left: 30px; top: 120px;
    font-family: "Montserrat", Arial, sans-serif;
    color: var(--ink-soft);
  }
  .contact__name {
    font-family: "Playfair Display", Georgia, serif;
    font-weight: 700; font-size: 19px; color: var(--navy);
    line-height: 1.1;
  }
  .contact__role { font-size: 10.5px; margin-top: 3px; }
  .contact__lines { margin-top: 16px; font-size: 10.5px; line-height: 1.55; }

  .divider {
    position: absolute; left: 30px; right: 30px; top: 218px;
    height: 1px; background: var(--navy);
  }

  .address {
    position: absolute; left: 330px; top: 232px;
    font-family: "Montserrat", Arial, sans-serif;
    font-size: 10.5px; line-height: 1.55; color: var(--ink-soft);
  }
</style>
</head>
<body>
<main class="stage">
  <section class="card card--front" aria-label="Fronte">
    <h1 class="wordmark"><span class="line-one">Vorian</span><span class="line-two">Partners</span></h1>
  </section>

  <section class="card card--back" aria-label="Retro">
    <div class="wordmark"><span class="line-one">Vorian</span><span class="line-two">Partners</span></div>
    <div class="contact">
      <p class="contact__name">Marcello Tavoletti</p>
      <p class="contact__role">CEO e Fondatore</p>
      <p class="contact__lines">m.tavoletti@vorian-partners.example<br>+39.331.584.2064</p>
    </div>
    <div class="divider"></div>
    <p class="address">Piazza Lunetti 7<br>20145 Milano</p>
  </section>
</main>
</body>
</html>
```